Brightmoor Learning Data Dashboard

Brightmoor Learning is a leading provider of digital curriculum and online courses to increase educational opportunities and achievement to students in grades K-12. Teachers and students access all course materials online.

School districts need greater visibility into the rate in which students are progressing through their courses, so school staff can better support students to complete courses at the required rate to keep them on track for graduation.
This can be accomplished by allowing school administrators to view a data dashboard and pull an on-demand report and see progress for a specified date range, relative to overall progress.

Within a specified date range, school administrators want to know if the student made more or less progress than in the period prior to the first date in the range.
School administrators also want to know if students are ahead or behind where they should be after the second date in the range.

Industry/Entity Type

Digital

```html
<!DOCTYPE html>
<html lang="en">
<head>
<meta charset="utf-8">
<title>Brightmoor Learning – Time Based Performance</title>
<link href="https://fonts.googleapis.com/css2?family=Roboto:wght@400;500;700&display=swap" rel="stylesheet">
<style>
:root{
  --brand:#5c5191;
  --brand-dark:#3e3466;
  --heading:#3d3466;
  --side-top:#d2ccec;
  --side-bottom:#ebe7fb;
  --tile-light:#e6e2f6;
  --ink:#222;
  --line:#dcdcdc;
  --field-line:#d6d6d6;
  --arrow-bg:#dedede;
  --footer:#000;
  --white:#fff;
}
*{box-sizing:border-box;margin:0;padding:0}
html,body{width:1200px;height:803px;overflow:hidden;background:var(--white)}
body{position:relative;font-family:'Roboto',sans-serif;color:var(--ink)}
.topbar{position:absolute;left:0;top:0;width:1200px;height:95px;background:var(--brand)}
.menu-toggle{position:absolute;left:0;top:0;width:74px;height:95px;background:var(--brand-dark)}
.menu-toggle svg{position:absolute;left:22px;top:36px}
.brand{position:absolute;left:93px;top:33px;display:flex;align-items:center;gap:8px;color:var(--white);font-size:17px;font-weight:500;letter-spacing:.3px}
.brand-dot{width:14px;height:14px;border-radius:50%;background:var(--white)}
.user{position:absolute;left:968px;top:21px;display:flex;align-items:center;gap:10px;color:var(--white);font-size:16px}
.avatar{width:52px;height:52px;border-radius:50%;background:radial-gradient(circle at 50% 45%,#e9c3a8,#8a4a2c 75%)}
.sidebar{position:absolute;left:0;top:95px;width:74px;height:668px;background:linear-gradient(to bottom,var(--side-top),var(--side-bottom))}
.nav-tile{height:63px;display:flex;align-items:center;justify-content:center;border-bottom:1px solid #ddd8f0}
.nav-tile.is-active{background:var(--brand)}
.nav-tile.is-light{background:var(--tile-light)}
.page-title{position:absolute;left:117px;top:128px;font-size:27px;font-weight:400;color:var(--ink)}
.download{position:absolute;left:881px;top:126px;width:234px;height:38px;background:var(--brand-dark);color:var(--white);font-size:17px;font-weight:500;letter-spacing:2.6px;display:flex;align-items:center;justify-content:center}
.filter-label{position:absolute;top:191px;font-size:14px;color:var(--ink);display:flex;align-items:center;gap:6px}
.radio{width:12px;height:12px;border-radius:50%;border:3px solid var(--brand-dark);background:var(--white)}
.radio.is-on{background:var(--brand-dark);border-color:var(--brand-dark)}
.select{position:absolute;top:213px;width:234px;height:38px;border:1px solid var(--field-line);font-size:12.5px;color:#444;display:flex;align-items:center;padding-left:17px}
.select-arrow{position:absolute;right:0;top:0;width:33px;height:100%;background:var(--arrow-bg);display:flex;align-items:center;justify-content:center}
.table-wrap{position:absolute;left:117px;top:284px;width:1083px;height:418px;overflow:hidden}
.report{border-collapse:collapse;table-layout:fixed;width:1280px}
.report th,.report td{border:1px solid var(--line);text-align:left;padding:0 0 0 17px;font-size:12.5px}
.report th{color:var(--heading);font-weight:500;font-size:11.5px;letter-spacing:.9px;text-transform:uppercase;line-height:1.4}
.report .group{color:var(--ink);font-size:13.5px;text-align:center;letter-spacing:.6px;padding:0;height:28px}
.report .period{color:var(--ink);text-align:center;padding:0;height:28px;font-size:12px}
.report .sub{height:27px}
.report tbody td{height:48px}
.report tbody tr.tall td{height:48.5px}
.scrollbar{position:absolute;left:117px;top:722px;width:1083px;height:20px;border:1px solid #aaa;background:linear-gradient(#f7f7f7,#e2e2e2)}
.scroll-thumb{position:absolute;left:73px;top:1px;width:205px;height:16px;border:1px solid #888;border-radius:2px;background:linear-gradient(#e8e8e8,#bdbdbd)}
.scroll-thumb::after{content:"";position:absolute;left:100px;top:4px;width:5px;height:7px;border-left:1px solid #555;border-right:1px solid #555}
.footer{position:absolute;left:0;top:763px;width:1200px;height:40px;background:var(--footer);color:var(--white);font-size:12px;display:flex;align-items:center;justify-content:center}
</style>
</head>
<body>
<header class="topbar">
  <div class="menu-toggle">
    <svg width="30" height="22" viewBox="0 0 30 22"><g stroke="#fff" stroke-width="2.4"><line x1="0" y1="2" x2="30" y2="2"/><line x1="0" y1="11" x2="30" y2="11"/><line x1="0" y1="20" x2="30" y2="20"/></g></svg>
  </div>
  <div class="brand"><span class="brand-dot"></span>Brightmoor Learning</div>
  <div class="user">
    <div class="avatar" role="img" aria-label="User profile photo"></div>
    <span>Jane Doe</span>
    <svg width="10" height="6" viewBox="0 0 10 6"><path d="M1 1l4 4 4-4" fill="none" stroke="#fff" stroke-width="1.5"/></svg>
  </div>
</header>

<nav class="sidebar">
  <div class="nav-tile is-active">
    <svg width="24" height="16" viewBox="0 0 24 16"><path d="M2 15a10 10 0 0 1 20 0z" fill="#fff"/><g fill="var(--brand)"><circle cx="6" cy="10" r="1.3"/><circle cx="9" cy="6" r="1.3"/><circle cx="15" cy="6" r="1.3"/><circle cx="18" cy="10" r="1.3"/><circle cx="12" cy="12" r="1.8"/></g><line x1="12" y1="12" x2="14" y2="5" stroke="var(--brand)" stroke-width="1.6"/></svg>
  </div>
  <div class="nav-tile is-light">
    <svg width="18" height="20" viewBox="0 0 18 20"><circle cx="9" cy="5.5" r="5" fill="var(--brand)"/><path d="M0 20a9 8 0 0 1 18 0z" fill="var(--brand)"/></svg>
  </div>
</nav>

<main>
  <h1 class="page-title">Time Based Performance</h1>
  <div class="download">DOWNLOAD FILE</div>

  <div class="filter-label" style="left:117px">School:</div>
  <div class="filter-label" style="left:372px"><span class="radio"></span>Observer:</div>
  <div class="filter-label" style="left:512px"><span class="radio is-on"></span>Teacher:</div>
  <div class="filter-label" style="left:626px">Filter Date 1:</div>
  <div class="filter-label" style="left:881px">Filter date 2:</div>

  <div class="select" style="left:117px">Choose a school...<span class="select-arrow"><svg width="10" height="6" viewBox="0 0 10 6"><path d="M1 1l4 4 4-4" fill="none" stroke="#666" stroke-width="1.3"/></svg></span></div>
  <div class="select" style="left:372px">Choose an observer...<span class="select-arrow"><svg width="10" height="6" viewBox="0 0 10 6"><path d="M1 1l4 4 4-4" fill="none" stroke="#666" stroke-width="1.3"/></svg></span></div>
  <div class="select" style="left:626px">2/27/18<span class="select-arrow"><svg width="10" height="6" viewBox="0 0 10 6"><path d="M1 1l4 4 4-4" fill="none" stroke="#666" stroke-width="1.3"/></svg></span></div>
  <div class="select" style="left:881px">3/6/18<span class="select-arrow"><svg width="10" height="6" viewBox="0 0 10 6"><path d="M1 1l4 4 4-4" fill="none" stroke="#666" stroke-width="1.3"/></svg></span></div>

  <div class="table-wrap">
    <table class="report">
      <colgroup>
        <col style="width:133px"><col style="width:110px"><col style="width:94px"><col style="width:143px">
        <col style="width:94px"><col style="width:77px"><col style="width:85px"><col style="width:86px">
        <col style="width:99px"><col style="width:82px"><col style="width:93px"><col style="width:184px">
      </colgroup>
      <thead>
        <tr>
          <th rowspan="3">Student Name</th><th rowspan="3">Observer</th><th rowspan="3">School</th><th rowspan="3">Course Title</th>
          <th rowspan="3">Current Grade</th><th rowspan="3">Raw Score</th><th rowspan="3">Course Start Date</th><th rowspan="3">Course End Date</th>
          <th colspan="4" class="group">PERCENT COMPLETE</th>
        </tr>
        <tr><th colspan="2" class="period">START - 2/27/18</th><th colspan="2" class="period" style="text-align:left;padding-left:17px">END - 3/6/18</th></tr>
        <tr class="sub"><th>Actual %</th><th>Goal %</th><th>Actual %</th><th>Goal %</th></tr>
      </thead>
      <tbody>
        <tr><td>Anthony Jones</td><td>Sam Cox</td><td>Rosemont</td><td>Algebra 1A</td><td>67.3%</td><td>70%</td><td>2/20/18</td><td>4/24/18</td><td>0%</td><td>10%</td><td>5%</td><td>20%</td></tr>
        <tr><td>Jose Alvarez</td><td>Sam Cox</td><td>Rosemont</td><td>Biology A</td><td>74.2%</td><td>83%</td><td>2/20/18</td><td>4/24/18</td><td>5%</td><td>10%</td><td>15%</td><td>20%</td></tr>
        <tr class="tall"><td>Maria Lee</td><td>Jema Interiano</td><td>Kennedy</td><td>US History A</td><td>82.3%</td><td>82.3%</td><td>2/20/18</td><td>4/24/18</td><td>15%</td><td>10%</td><td>20%</td><td>20%</td></tr>
        <tr class="tall"><td>Marcus Smith</td><td>Jema Interiano</td><td>Kennedy</td><td>Algebra 1A</td><td>91.0%</td><td>95.0%</td><td>2/20/18</td><td>4/24/18</td><td>9%</td><td>10%</td><td>11%</td><td>20%</td></tr>
        <tr class="tall"><td>Juan Rodriguez</td><td>Meg Johnson</td><td>Burbank</td><td>Language Arts 10 A</td><td>94.5%</td><td>94.5%</td><td>2/20/18</td><td>4/24/18</td><td>11%</td><td>10%</td><td>28%</td><td>20%</td></tr>
        <tr class="tall"><td>Jose Carlos</td><td>Meg Johnson</td><td>Burbank</td><td>Language Arts 10B</td><td>80%</td><td>85%</td><td>2/20/18</td><td>4/24/18</td><td>5%</td><td>10%</td><td>10%</td><td>20%</td></tr>
        <tr class="tall"><td>Julie Carns</td><td>Meg Johnson</td><td>Burbank</td><td>US History 1A</td><td>75%</td><td>80%</td><td>2/20/18</td><td>4/24/18</td><td>10%</td><td>10%</td><td>20%</td><td>20%</td></tr>
      </tbody>
    </table>
  </div>

  <div class="scrollbar">
    <svg style="position:absolute;left:3px;top:4px" width="6" height="10" viewBox="0 0 6 10"><path d="M6 0v10L0 5z" fill="#222"/></svg>
    <div class="scroll-thumb"></div>
    <svg style="position:absolute;right:3px;top:4px" width="6" height="10" viewBox="0 0 6 10"><path d="M0 0v10l6-5z" fill="#222"/></svg>
  </div>
</main>

<footer class="footer">Brightmoor Learning © 2018 &nbsp;|&nbsp; All Rights Reserved.</footer>
</body>
</html>
```